Tree Pruning Website

We need a website for a tree Arborist, pruning company called Hollow Ridge Groundcare. We look after all types of trees, knock down trees and prune trees. Our target market is from domestic clients to government clients and everything in between.

We would like to see the use of our main colours which are orange and green

We are not looking forward in seeing a template that we have seen before but a unique template. We have designed 5 templates ourselves and we wish for the design community to take our designs to the next level.

We have also designed a template for things that **we are not** looking for (Version 4)

To make it fair for everyone, we are also not giving out any participation payments as we have had. One winner will take all of the payment!!!

I Have attached a image of the designs and a image of a tree.

We are just looking at the PSD file been developed. We have our own team who can slice the image up into a HTML format.

Target Market(s)

Everyone who needs to cut down a tree

Industry/Entity Type

Government

Requirements
Must have
• Logo on front page
A List of our services
jQuery slider on page
Phone Number on every page

```html
<!DOCTYPE html>
<html lang="en">
<head>
<meta charset="utf-8">
<title>Hollow Ridge Groundcare</title>
<link rel="stylesheet" href="https://fonts.googleapis.com/css2?family=Noto+Serif:ital,wght@1,400&family=Open+Sans:wght@400&family=Roboto+Slab:wght@300;400&family=Ubuntu:wght@400&display=swap">
<style>
  :root {
    --orange: #e8820e;
    --green: #3f7a2b;
    --green-dark: #2f6420;
    --footer: #47803a;
    --footer-text: #e6efd9;
    --beige: #f2e0bd;
    --beige-light: #f7ead0;
    --panel: #fdfaf4;
    --line: #e6dccb;
    --ink: #3a3a3a;
    --muted: #7a6e5e;
  }
  * { box-sizing: border-box; margin: 0; padding: 0; }
  html, body { width: 1172px; height: 1200px; overflow: hidden; }
  body { position: relative; background: #fff; font-family: "Open Sans", sans-serif; color: var(--ink); }
  .abs { position: absolute; }

  .masthead { left: 0; top: 0; width: 1172px; height: 576px;
    background: linear-gradient(180deg, var(--beige-light), var(--beige)); }
  .masthead::after { content: ""; position: absolute; left: 0; right: 0; bottom: 0; height: 8px;
    background: linear-gradient(180deg, var(--beige), #ead4a8); }

  .brand { left: 150px; top: 70px; width: 150px; text-align: center;
    font-family: "Roboto Slab", serif; font-weight: 400; font-size: 15px; line-height: 17px; color: var(--green); }
  .brand-dot { left: 208px; top: 22px; width: 34px; height: 34px; border-radius: 50%; background: var(--green); }

  .social { width: 27px; height: 27px; border-radius: 50%; background: var(--orange); }
  .call-top { left: 782px; top: 60px; font-family: "Roboto Slab", serif; font-weight: 300; font-size: 15px; color: var(--orange); white-space: nowrap; }
  .call-top .num { color: var(--ink); font-size: 17px; margin-left: 4px; }
  .call-top svg { vertical-align: -2px; margin-left: 4px; }

  .main-nav { top: 100px; font-family: "Roboto Slab", serif; font-weight: 300; font-size: 13px; color: var(--ink); letter-spacing: .3px; }

  .slider-frame { left: 153px; top: 166px; width: 576px; height: 388px; background: #fff;
    box-shadow: 0 1px 4px rgba(0,0,0,.25); }
  .slide { left: 8px; top: 7px; width: 560px; height: 373px;
    background: linear-gradient(135deg, #3b5a2a 0%, #7d8a6a 35%, #d8cfbd 55%, #4d6a88 80%, #2f4d2a 100%); }

  .contact { left: 759px; top: 166px; width: 247px; height: 388px; background: var(--panel);
    border-radius: 3px; box-shadow: 0 1px 3px rgba(0,0,0,.15); overflow: hidden; }
  .contact-head { height: 43px; background: var(--green); color: #fff; text-align: center;
    font-family: "Roboto Slab", serif; font-weight: 400; font-size: 16px; line-height: 46px; }
  .field { position: absolute; left: 15px; width: 216px; height: 27px; background: #fff;
    border: 1px solid var(--line); border-radius: 2px; font-family: "Ubuntu", sans-serif; font-size: 11.5px;
    padding: 6px 10px; color: var(--ink); }
  .field.msg { height: 110px; }
  .send { position: absolute; left: 15px; top: 305px; width: 216px; height: 40px; border-radius: 2px;
    background: linear-gradient(180deg, #4b8a36, var(--green-dark)); color: #fff; text-align: center;
    font-family: "Roboto Slab", serif; font-size: 15px; line-height: 40px; }
  .call-box { position: absolute; left: 19px; top: 354px; font-family: "Roboto Slab", serif; font-weight: 300;
    font-size: 14px; color: var(--orange); white-space: nowrap; }
  .call-box .num { color: var(--ink); font-size: 16px; margin-left: 16px; }

  .foliage { border-radius: 50%; background: radial-gradient(circle, rgba(120,170,60,.35), rgba(120,170,60,0) 70%); }

  .panel { background: var(--panel); border: 1px solid var(--line); border-radius: 3px; }
  .ribbon { height: 30px; background: var(--orange); color: #fff; font-family: "Roboto Slab", serif;
    font-weight: 400; font-size: 16px; line-height: 31px; padding-left: 40px; white-space: nowrap;
    clip-path: polygon(0 0, 100% 0, 93% 50%, 100% 100%, 0 100%); }
  .fold { width: 0; height: 0; border-top: 12px solid #9c5608; border-left: 12px solid transparent; }

  .service { font-family: "Ubuntu", sans-serif; font-size: 15px; color: var(--ink); white-space: nowrap; letter-spacing: .3px; }
  .service .n { display: inline-block; width: 16px; height: 16px; border-radius: 50%; background: var(--orange);
    color: #fff; font-size: 10px; line-height: 16px; text-align: center; margin-right: 8px; vertical-align: 1px; }

  .intro-title { left: 170px; top: 815px; width: 490px; font-family: "Roboto Slab", serif; font-weight: 300;
    font-size: 16.5px; line-height: 18px; letter-spacing: .4px; color: var(--green); }
  .intro-text { left: 170px; top: 864px; width: 556px; font-size: 11.2px; line-height: 15.5px; color: var(--ink); }

  .quote { left: 774px; width: 226px; font-family: "Noto Serif", serif; font-style: italic; font-size: 12px;
    line-height: 15.5px; color: var(--muted); }
  .quote-by { left: 774px; width: 210px; text-align: right; font-family: "Roboto Slab", serif; font-weight: 300;
    font-size: 14px; color: var(--green); }
  .divider { left: 774px; width: 216px; border-top: 1px dotted #c9b99a; }

  .site-footer { left: 0; top: 1012px; width: 1172px; height: 188px; background: var(--footer); color: var(--footer-text);
    font-family: "Roboto Slab", serif; font-weight: 300; }
  .footer-brand { position: absolute; left: 190px; top: 90px; width: 140px; text-align: center; font-size: 15px;
    line-height: 17px; color: #a9c79a; font-weight: 400; }
  .footer-dot { position: absolute; left: 240px; top: 28px; width: 40px; height: 40px; border-radius: 50%; background: #6d9c5b; }
  .footer-nav { position: absolute; top: 37px; font-size: 11px; letter-spacing: .3px; }
  .footer-info { position: absolute; font-size: 10.5px; letter-spacing: .3px; line-height: 13px; }
  .footer-social { position: absolute; top: 29px; width: 27px; height: 27px; border-radius: 50%; background: #2f5c25; }
</style>
</head>
<body>
  <div class="abs masthead"></div>

  <div class="abs brand-dot"></div>
  <div class="abs brand">HOLLOW RIDGE<br>GROUNDCARE</div>

  <div class="abs social" style="left:705px;top:58px"></div>
  <div class="abs social" style="left:738px;top:58px"></div>
  <div class="abs call-top">CALL US ON
    <svg width="14" height="14" viewBox="0 0 24 24" fill="none" stroke="#e8820e" stroke-width="2"><path d="M5 3h4l2 5-3 2a12 12 0 0 0 6 6l2-3 5 2v4a2 2 0 0 1-2 2A18 18 0 0 1 3 5a2 2 0 0 1 2-2z"/></svg><span class="num">08 5550 1234</span></div>

  <nav>
    <div class="abs main-nav" style="left:472px">HOME</div>
    <div class="abs main-nav" style="left:554px">ABOUT US</div>
    <div class="abs main-nav" style="left:663px">OUR SERVICES</div>
    <div class="abs main-nav" style="left:798px">GET A QUOTE</div>
    <div class="abs main-nav" style="left:923px">CONTACT US</div>
  </nav>

  <div class="abs slider-frame">
    <div class="abs slide" role="img" aria-label="Photo looking up into tall pale-barked gum trees against a blue sky"></div>
  </div>

  <div class="abs contact">
    <div class="contact-head">CONTACT US TODAY</div>
    <div class="field" style="top:62px">Name</div>
    <div class="field" style="top:101px">email</div>
    <div class="field" style="top:140px">Phone</div>
    <div class="field msg" style="top:181px">Message</div>
    <div class="send">SEND</div>
    <div class="call-box">CALL US ON<span class="num">08 5550 1234</span></div>
  </div>

  <div class="abs foliage" role="img" aria-label="Scattered green leaves" style="left:1000px;top:415px;width:100px;height:110px"></div>
  <div class="abs foliage" role="img" aria-label="Scattered green leaves" style="left:0;top:945px;width:176px;height:70px"></div>

  <section>
    <div class="abs panel" style="left:165px;top:603px;width:564px;height:193px"></div>
    <div class="abs ribbon" style="left:153px;top:615px;width:207px">OUR SERVICES</div>
    <div class="abs fold" style="left:153px;top:645px"></div>

    <div class="abs service" style="left:193px;top:663px"><span class="n">1</span>Diagnosis</div>
    <div class="abs service" style="left:325px;top:663px"><span class="n">2</span>Treatment</div>
    <div class="abs service" style="left:461px;top:663px"><span class="n">3</span>Purning</div>
    <div class="abs service" style="left:580px;top:663px"><span class="n">4</span>Tree Removal</div>
    <div class="abs service" style="left:193px;top:703px"><span class="n">5</span>Stump Removal</div>
    <div class="abs service" style="left:371px;top:703px"><span class="n">6</span>Cable &amp; Bracing</div>
    <div class="abs service" style="left:546px;top:703px"><span class="n">7</span>Arboris Consults</div>
    <div class="abs service" style="left:193px;top:741px"><span class="n">8</span>Tree Protection</div>

    <h2 class="abs intro-title">Lorem Ipsum is simply dummy text of the printing and typesetting industry.</h2>
    <p class="abs intro-text">Lorem Ipsum is simply dummy text of the printing and typesetting industry. Lorem Ipsum has been the industry's standard dummy text ever since the 1500s, when an unknown printer took a galley of type and scrambled it to make a type specimen book. It has survived not only five centuries, but also the leap into electronic typesetting, remaining essentially unchanged. It was popularised in the 1960s with the release of Inkwell sheets containing Lorem Ipsum passages, and more recently with desktop publishing software like Pagewright Studio including versions of Lorem Ipsum.</p>
  </section>

  <aside>
    <div class="abs panel" style="left:759px;top:603px;width:246px;height:358px"></div>
    <div class="abs ribbon" style="left:748px;top:615px;width:237px;padding-left:28px">What our clients say</div>
    <div class="abs fold" style="left:748px;top:645px"></div>

    <p class="abs quote" style="top:659px">Lorem Ipsum is simply dummy text of the printing and typesetting industry. Lorem Ipsum has been the industry's standard dummy text ever since</p>
    <div class="abs quote-by" style="top:727px">-Clara Whitmore</div>
    <div class="abs divider" style="top:754px"></div>
    <p class="abs quote" style="top:763px">Lorem Ipsum is simply dummy text of the printing and typesetting industry. Lorem Ipsum has been the industry's standard dummy text ever since</p>
    <div class="abs quote-by" style="top:830px">-Clara Whitmore</div>
    <div class="abs divider" style="top:857px"></div>
    <p class="abs quote" style="top:866px">Lorem Ipsum is simply dummy text of the printing and typesetting industry. Lorem Ipsum has been the industry's standard dummy text ever since</p>
    <div class="abs quote-by" style="top:934px">-Clara Whitmore</div>
  </aside>

  <footer class="abs site-footer">
    <div class="footer-dot"></div>
    <div class="footer-brand">HOLLOW RIDGE<br>GROUNDCARE</div>
    <div class="footer-nav" style="left:342px">HOME</div>
    <div class="footer-nav" style="left:412px">ABOUT US</div>
    <div class="footer-nav" style="left:505px">OUR SERVICES</div>
    <div class="footer-nav" style="left:621px">GET A QUOTE</div>
    <div class="footer-nav" style="left:728px">CONTACT US</div>
    <div class="footer-social" style="left:846px"></div>
    <div class="footer-social" style="left:879px"></div>
    <div class="footer-info" style="left:342px;top:68px;width:175px">14 Fernhill Road Oakvale,<br>WA 6999</div>
    <div class="footer-info" style="left:537px;top:68px">Phone&nbsp; 08 5550 1234</div>
    <div class="footer-info" style="left:677px;top:68px">fax 08 5550 1234</div>
    <div class="footer-info" style="left:342px;top:108px">COPYRIGHT 2013. HOLLOW RIDGE GROUNDCARE</div>
  </footer>
</body>
</html>
```